DPM Marketing Postcard

Design a 2 Sided marketing postcard for our Real estate management caompany. Looking for a professional yet fresh look that will be printed on a 6"x9" glossy flier

Contact information is www.dunkeldmanagement-example.com dunkeldmanagement@dunkeldmail-example.com and 312-480-7193

WE are targeting small condo and town home properties to take on their administrative responsibilities of management

```html
<!DOCTYPE html>
<html lang="en">
<head>
<meta charset="utf-8">
<title>DPM Marketing Postcard</title>
<link href="https://fonts.googleapis.com/css2?family=Montserrat:wght@400;600;700;800&family=Open+Sans:wght@400;600;700&family=Libre+Baskerville:wght@700&display=swap" rel="stylesheet">
<style>
:root{
  --navy:#1c3578;
  --blue:#2d56b3;
  --sky:#5d8bdb;
  --ink:#23335c;
  --grey:#7a7f8a;
  --stage:#eceef2;
  --card:#ffffff;
}
*{margin:0;padding:0;box-sizing:border-box}
html,body{width:804px;height:1200px;overflow:hidden;background:var(--stage)}
body{position:relative;font-family:"Open Sans",Arial,sans-serif;color:var(--ink)}
.card{position:absolute;left:48px;width:708px;height:525px;background:var(--card);overflow:hidden;box-shadow:0 6px 18px rgba(20,30,60,.18)}
.card--front{top:50px}
.card--back{top:622px}

/* front */
.brand{position:absolute;font-family:"Montserrat",Arial,sans-serif;font-weight:700;color:var(--blue);text-transform:uppercase;letter-spacing:.3px}
.brand strong{color:var(--navy);font-weight:800}
.front-brand{left:38px;top:24px;font-size:13px;white-space:nowrap}
.tagline{position:absolute;left:38px;top:46px;width:380px;font-family:"Libre Baskerville",Georgia,serif;font-size:12.5px;line-height:1.35;color:var(--navy)}
.hero-photo{position:absolute;left:450px;top:0;width:258px;height:230px;background:linear-gradient(160deg,#4f7fd0 0%,#1f3f8c 55%,#8fb2e8 100%);border-bottom-left-radius:120px 230px;border-left:7px solid var(--blue)}
.who{position:absolute;left:0;top:95px;width:190px;height:125px;background:var(--navy);color:#fff;font-family:"Montserrat",Arial,sans-serif;padding:24px 0 0 40px;font-size:30px;line-height:1.1}
.who b{font-weight:800;display:block}
.who span{font-weight:400}
.who-text{position:absolute;left:190px;top:95px;width:250px;height:125px;background:var(--blue);color:#fff;font-size:9.5px;line-height:1.3;padding:10px 12px}
.who-text p{margin-bottom:6px}
.col-head{position:absolute;font-family:"Montserrat",Arial,sans-serif;font-weight:800;font-size:14px;color:var(--navy);text-transform:uppercase;display:flex;align-items:center;gap:7px}
.col-head i{width:9px;height:9px;background:var(--blue);display:inline-block}
.list{position:absolute;list-style:none;font-size:9.2px;line-height:1.32;color:var(--ink)}
.list li{position:relative;padding-left:14px;margin-bottom:6px}
.list li::before{content:"";position:absolute;left:0;top:3px;width:6px;height:6px;background:var(--blue)}
.why-list{left:30px;top:264px;width:190px}
.what-list{left:250px;top:264px;width:430px}
.what-list li{margin-bottom:7px}
.building-photo{position:absolute;left:30px;top:404px;width:110px;height:52px;background:linear-gradient(180deg,#9db9e6,#445f9c)}
.phone{position:absolute;left:30px;top:464px;display:flex;align-items:center;gap:8px;font-family:"Montserrat",Arial,sans-serif;font-weight:800;font-size:17px;color:var(--navy)}
.front-wave{position:absolute;left:0;bottom:0;width:708px;height:34px}

/* back */
.back-arc{position:absolute;left:0;top:0;width:708px;height:525px}
.back-brand{left:38px;top:38px;font-size:19px;line-height:1.3}
.return-address{position:absolute;left:492px;top:40px;font-size:15px;line-height:1.4;color:var(--grey);font-style:normal}
.mail-lines{position:absolute;left:492px;top:200px;width:180px}
.mail-lines span{display:block;height:1px;background:#c6cad3;margin-bottom:26px}
.offer-list{left:38px;top:150px;width:360px;font-size:10.5px}
.offer-list li{margin-bottom:9px}
.contacts{position:absolute;left:38px;top:420px;list-style:none;font-size:11.5px;font-weight:700;color:var(--navy)}
.contacts li{display:flex;align-items:center;gap:8px;margin-bottom:6px}
.contacts svg{width:13px;height:13px}
</style>
</head>
<body>

<section class="card card--front">
  <div class="brand front-brand">Dunkeld Property <strong>Management LLC ("DPM")</strong></div>
  <p class="tagline">Improve compliance, Reporting, and Communication amongst all owners and board members</p>

  <div class="hero-photo" role="img" aria-label="Businessman in a suit beside a model of city towers"></div>

  <div class="who"><span>WHO</span><b>WE ARE</b></div>
  <div class="who-text">
    <p>A professional services organization with a focus on small (5-15 unit) residential buildings</p>
    <p>Over 18 years of combined experience in real estate and property management</p>
    <p>Professional, courteous, timely service that is technologically driven</p>
  </div>

  <div class="col-head" style="left:30px;top:238px"><i></i>Why use DPM?</div>
  <ul class="list why-list">
    <li>Owners are busy people who would rather not handle association tasks or chase fellow owners on related matters</li>
    <li>Low monthly fees tailored to your needs</li>
    <li>The association's board of directors maintains control of all decision-making</li>
  </ul>

  <div class="col-head" style="left:250px;top:238px"><i></i>What we do:</div>
  <ul class="list what-list">
    <li>Remove the administrative burden of managing small residential buildings</li>
    <li>Utilize economies of scale to reduce expenses for all owners across a wide variety of service providers</li>
    <li>Collect all assessments and pay all bills</li>
    <li>Provide monthly accounting reconciliation and reporting</li>
    <li>Provide access to DPM's client portal with a central repository of all association materials (bylaws, financials, meeting minutes, communications, etc)</li>
    <li>Issue 1099s to all contractors as required by law</li>
    <li>Prepare year-end financial statements</li>
    <li>Lender and 22.1 documents for mortgage companies and sales</li>
  </ul>

  <div class="building-photo" role="img" aria-label="Small condominium building exterior"></div>
  <div class="phone">
    <svg width="18" height="18" viewBox="0 0 24 24" aria-hidden="true"><path fill="#1c3578" d="M6.6 10.8a15.1 15.1 0 0 0 6.6 6.6l2.2-2.2c.3-.3.7-.4 1-.2 1.1.4 2.3.6 3.6.6.6 0 1 .4 1 1V20c0 .6-.4 1-1 1A17 17 0 0 1 3 4c0-.6.4-1 1-1h3.5c.6 0 1 .4 1 1 0 1.3.2 2.5.6 3.6.1.3 0 .7-.2 1z"/></svg>
    312-480-7193
  </div>

  <svg class="front-wave" viewBox="0 0 708 34" preserveAspectRatio="none" aria-hidden="true">
    <path d="M0 26 C200 8 450 38 708 18 L708 34 L0 34Z" fill="#1c3578"/>
    <path d="M0 20 C200 2 450 32 708 12" fill="none" stroke="#5d8bdb" stroke-width="3"/>
  </svg>
</section>

<section class="card card--back">
  <svg class="back-arc" viewBox="0 0 708 525" aria-hidden="true">
    <circle cx="170" cy="265" r="300" fill="none" stroke="#1c3578" stroke-width="18"/>
    <circle cx="170" cy="265" r="284" fill="none" stroke="#5d8bdb" stroke-width="5"/>
  </svg>

  <div class="brand back-brand">Dunkeld Property<br><strong>Management LLC ("DPM")</strong></div>

  <address class="return-address">
    14 Larchmont Court<br>Elmhurst,<br>IL 60126
  </address>

  <div class="mail-lines"><span></span><span></span><span></span><span></span><span></span></div>

  <ul class="list offer-list">
    <li>Cost effective property management solution for 5-15 unit buildings</li>
    <li>Prices starting as low as $150/month</li>
    <li>Utilize our economies of scale to reduce costs across vendors (trash, insurance, maintenance, etc)</li>
    <li>Eliminate the unfair burden placed on a few owners to do all the work while others do none</li>
    <li>Improve communication amongst all owners and board members</li>
    <li>The association's board of directors maintains all decision-making power</li>
    <li>Utilize our vetted service providers for prompt job completion and fair pricing</li>
  </ul>

  <ul class="contacts">
    <li><svg viewBox="0 0 24 24" aria-hidden="true"><path fill="#2d56b3" d="M6.6 10.8a15.1 15.1 0 0 0 6.6 6.6l2.2-2.2c.3-.3.7-.4 1-.2 1.1.4 2.3.6 3.6.6.6 0 1 .4 1 1V20c0 .6-.4 1-1 1A17 17 0 0 1 3 4c0-.6.4-1 1-1h3.5c.6 0 1 .4 1 1 0 1.3.2 2.5.6 3.6.1.3 0 .7-.2 1z"/></svg>312-480-7193</li>
    <li><svg viewBox="0 0 24 24" aria-hidden="true"><rect x="2" y="5" width="20" height="14" rx="2" fill="#2d56b3"/><path d="M3 6l9 7 9-7" fill="none" stroke="#fff" stroke-width="2"/></svg>dunkeldmanagement@dunkeldmail-example.com</li>
    <li><svg viewBox="0 0 24 24" aria-hidden="true"><circle cx="12" cy="12" r="10" fill="#2d56b3"/><path d="M2 12h20M12 2c3 3 3 17 0 20M12 2c-3 3-3 17 0 20" fill="none" stroke="#fff" stroke-width="1.5"/></svg>www.dunkeldmanagement-example.com</li>
  </ul>
</section>

</body>
</html>
```